Create a banner for a Gmail email signature

We need a graphic design to use in a solicitor's email signature. The banner will incorporate a head shot of the solicitor as well as the law firm's logo and contact details. The solicitor's photo and law firm's logo are uploaded in the task.

```html
<!DOCTYPE html>
<html lang="en">
<head>
<meta charset="utf-8">
<title>Solicitor Email Signature Banners</title>
<link rel="stylesheet" href="https://fonts.googleapis.com/css2?family=Outfit:wght@400;600&display=swap">
<style>
  :root {
    --brand: #8b0a4f;
    --ink: #111111;
    --paper: #ffffff;
    --photo-light: #d9c7b8;
    --photo-dark: #3b4a6b;
  }
  html, body {
    margin: 0;
    padding: 0;
    width: 1200px;
    height: 927px;
    overflow: hidden;
    background: var(--paper);
    font-family: "Outfit", sans-serif;
  }
  .canvas {
    position: relative;
    width: 1200px;
    height: 927px;
  }
  .signature {
    position: absolute;
    left: 135px;
    width: 930px;
    height: 317px;
    background: var(--paper);
    box-shadow: 0 0 40px rgba(0, 0, 0, 0.08);
  }
  .signature--round { top: 126px; }
  .signature--square { top: 484px; }
  .signature__shapes {
    position: absolute;
    inset: 0;
  }
  .identity__name {
    position: absolute;
    left: 276px;
    top: 70px;
    margin: 0;
    font-size: 31px;
    line-height: 1;
    font-weight: 600;
    color: var(--brand);
    letter-spacing: 0.2px;
  }
  .identity__role {
    position: absolute;
    left: 277px;
    top: 98px;
    margin: 0;
    font-size: 24px;
    line-height: 1;
    font-weight: 400;
    color: var(--brand);
  }
  .firm-name {
    position: absolute;
    right: 43px;
    top: 64px;
    margin: 0;
    font-size: 27px;
    line-height: 1;
    font-weight: 400;
    color: var(--brand);
    letter-spacing: 0.5px;
  }
  .contact-list {
    list-style: none;
    margin: 0;
    padding: 0;
  }
  .contact-list__item {
    position: absolute;
    left: 308px;
    font-size: 20px;
    line-height: 1;
    color: var(--ink);
    white-space: nowrap;
  }
  .contact-list__item:nth-child(1) { top: 155px; }
  .contact-list__item:nth-child(2) { top: 187px; }
  .contact-list__item:nth-child(3) { top: 218px; }
  .contact-list__item:nth-child(4) { top: 249px; }
</style>
</head>
<body>
<main class="canvas">

  <!-- Signature with round portrait -->
  <section class="signature signature--round">
    <svg class="signature__shapes" width="930" height="317" viewBox="0 0 930 317" aria-hidden="false">
      <defs>
        <linearGradient id="portrait-tone-a" x1="0" y1="0" x2="1" y2="1">
          <stop offset="0" stop-color="var(--photo-light)"/>
          <stop offset="0.55" stop-color="#c9a99a"/>
          <stop offset="1" stop-color="var(--photo-dark)"/>
        </linearGradient>
      </defs>
      <path class="accent-frame" d="M0 0 H129 A26 26 0 0 1 155 26 V273 A20 20 0 0 0 175 293 H930 V317 H0 Z" fill="var(--brand)"/>
      <circle class="portrait-ring" cx="146" cy="159" r="108" fill="var(--paper)"/>
      <circle class="portrait" cx="146" cy="159" r="99" fill="url(#portrait-tone-a)" role="img" aria-label="Head-shot photo of the solicitor"/>
      <line class="divider" x1="284" y1="132" x2="886" y2="132" stroke="var(--ink)" stroke-width="1.5"/>
      <g class="contact-icons" fill="var(--brand)">
        <circle cx="286" cy="164" r="11"/>
        <circle cx="286" cy="196" r="11"/>
        <circle cx="286" cy="227" r="11"/>
        <circle cx="286" cy="258" r="11"/>
      </g>
      <g class="contact-glyphs" fill="none" stroke="var(--paper)" stroke-width="1.4" stroke-linecap="round" stroke-linejoin="round">
        <path d="M281.5 159.5 q-1 4 4 8.5 q4.5 4 8.5 3 l0.5 -2 l-3 -1.5 l-1.5 1.5 q-3 -1.5 -5 -4.5 l1.5 -1.5 l-1.5 -3 z" fill="var(--paper)" stroke="none"/>
        <rect x="280" y="192" width="12" height="8.5" rx="1"/>
        <path d="M280 192.5 L286 197 L292 192.5"/>
        <circle cx="286" cy="227" r="6"/>
        <ellipse cx="286" cy="227" rx="2.6" ry="6"/>
        <path d="M280 227 H292 M281 224 H291 M281 230 H291"/>
        <path d="M286 265 C281 259 281 256 281 254.5 A5 5 0 0 1 291 254.5 C291 256 291 259 286 265 Z" fill="var(--paper)" stroke="none"/>
        <circle cx="286" cy="254.5" r="1.8" fill="var(--brand)" stroke="none"/>
      </g>
      <g class="social-links" fill="var(--brand)">
        <circle cx="752" cy="258" r="24" role="img" aria-label="Social profile link"/>
        <circle cx="809" cy="258" r="24" role="img" aria-label="Social profile link"/>
        <circle cx="866" cy="258" r="24" role="img" aria-label="Social profile link"/>
      </g>
    </svg>
    <h2 class="identity__name">YOUR NAME</h2>
    <p class="identity__role">Solicitor</p>
    <p class="firm-name">BAYVIEW FAMILY LAW</p>
    <ul class="contact-list">
      <li class="contact-list__item">000-000000</li>
      <li class="contact-list__item">youremail@mil.com</li>
      <li class="contact-list__item">your website.com</li>
      <li class="contact-list__item">Your Address</li>
    </ul>
  </section>

  <!-- Signature with square portrait -->
  <section class="signature signature--square">
    <svg class="signature__shapes" width="930" height="317" viewBox="0 0 930 317">
      <defs>
        <linearGradient id="portrait-tone-b" x1="0" y1="0" x2="1" y2="1">
          <stop offset="0" stop-color="var(--photo-light)"/>
          <stop offset="0.55" stop-color="#c9a99a"/>
          <stop offset="1" stop-color="var(--photo-dark)"/>
        </linearGradient>
      </defs>
      <rect class="accent-block" x="0" y="0" width="191" height="317" fill="var(--brand)"/>
      <rect class="portrait-frame" x="45" y="63" width="206" height="206" fill="var(--paper)"/>
      <rect class="portrait" x="56" y="74" width="184" height="184" fill="url(#portrait-tone-b)" role="img" aria-label="Head-shot photo of the solicitor"/>
      <rect class="divider" x="251" y="132" width="679" height="5" fill="var(--brand)"/>
      <g class="contact-icons" fill="var(--brand)">
        <circle cx="286" cy="164" r="11"/>
        <circle cx="286" cy="196" r="11"/>
        <circle cx="286" cy="227" r="11"/>
        <circle cx="286" cy="258" r="11"/>
      </g>
      <g class="contact-glyphs" fill="none" stroke="var(--paper)" stroke-width="1.4" stroke-linecap="round" stroke-linejoin="round">
        <path d="M281.5 159.5 q-1 4 4 8.5 q4.5 4 8.5 3 l0.5 -2 l-3 -1.5 l-1.5 1.5 q-3 -1.5 -5 -4.5 l1.5 -1.5 l-1.5 -3 z" fill="var(--paper)" stroke="none"/>
        <rect x="280" y="192" width="12" height="8.5" rx="1"/>
        <path d="M280 192.5 L286 197 L292 192.5"/>
        <circle cx="286" cy="227" r="6"/>
        <ellipse cx="286" cy="227" rx="2.6" ry="6"/>
        <path d="M280 227 H292 M281 224 H291 M281 230 H291"/>
        <path d="M286 265 C281 259 281 256 281 254.5 A5 5 0 0 1 291 254.5 C291 256 291 259 286 265 Z" fill="var(--paper)" stroke="none"/>
        <circle cx="286" cy="254.5" r="1.8" fill="var(--brand)" stroke="none"/>
      </g>
      <g class="social-links" fill="var(--brand)">
        <circle cx="752" cy="258" r="24" role="img" aria-label="Social profile link"/>
        <circle cx="809" cy="258" r="24" role="img" aria-label="Social profile link"/>
        <circle cx="866" cy="258" r="24" role="img" aria-label="Social profile link"/>
      </g>
    </svg>
    <h2 class="identity__name">YOUR NAME</h2>
    <p class="identity__role">Solicitor</p>
    <p class="firm-name">BAYVIEW FAMILY LAW</p>
    <ul class="contact-list">
      <li class="contact-list__item">000-000000</li>
      <li class="contact-list__item">youremail@mil.com</li>
      <li class="contact-list__item">your website.com</li>
      <li class="contact-list__item">Your Address</li>
    </ul>
  </section>

</main>
</body>
</html>
```